Vintage watches retailer name and baseline

Based in Cambodia, i open a small online watches shop, means i buy old watches i scout in south east asia, and resell in my online shop.
I wish to get an attractive name for my shop, something trendy, who make you travelling across the time. The shop have to seen as a boutique shop, full of products, the client taking time to look for all products might find a collector. Its not a luxury shop, the brands are KAVRO, LOMBARD mostly even if some pieces are unique 80% of the stock are old watches, all sold with boxes, guarantee, and in perfect condition to be weared.
i created 4 collections one for the watches produced between 1920-1930 / 1930 - 1940 / 1950-1960/ 1960-1970.
I am myself french-portguese, Cambodia use to be a french protectorat, my name il bastien larrue quintal.
Buying a vintage watch is actually a smart move, the price can be affordable ( from 50$ ) and the brand manufacturer used to work with better materials than today, means your modern watch will hardly cross a life time period when the old ones does.
Thanks by advance

```html
<!DOCTYPE html>
<html lang="en">
<head>
<meta charset="utf-8">
<title>Tempoquintal – Vintage Watches</title>
<link rel="stylesheet" href="https://fonts.googleapis.com/css2?family=PT+Sans:ital,wght@0,400;1,400&display=swap">
<style>
  :root {
    --ink: #111111;
    --mark-ink: #4a4a4a;
    --bg-light: #ffffff;
    --bg-mid: #ececec;
    --bg-shade: #c9c9c9;
    --floor: #f1f1f1;
  }
  * { margin: 0; padding: 0; box-sizing: border-box; }
  html, body { width: 1200px; height: 725px; overflow: hidden; }
  body { font-family: "PT Sans", sans-serif; color: var(--ink); }

  .card {
    position: relative;
    width: 1200px;
    height: 725px;
    overflow: hidden;
    background:
      radial-gradient(ellipse 520px 300px at 600px 330px, rgba(255,255,255,0.95), rgba(255,255,255,0) 70%),
      linear-gradient(180deg,
        var(--bg-mid) 0%,
        #f4f4f4 35%,
        var(--bg-light) 54%,
        #e2e2e2 74%,
        var(--bg-shade) 84%,
        #dcdcdc 87%,
        var(--floor) 94%,
        #e8e8e8 100%);
  }

  .brand-mark {
    position: absolute;
    left: 26px;
    top: 72px;
    display: flex;
    align-items: center;
    gap: 10px;
    font-size: 24px;
    font-weight: 400;
    color: var(--mark-ink);
  }
  .brand-mark .dot {
    width: 16px;
    height: 16px;
    border-radius: 50%;
    background: var(--mark-ink);
  }

  .shop-label {
    position: absolute;
    left: 244px;
    top: 162px;
    font-size: 36px;
    font-style: italic;
    line-height: 1;
  }

  .shop-name {
    position: absolute;
    left: 240px;
    top: 200px;
    font-size: 128px;
    font-style: italic;
    font-weight: 400;
    line-height: 1;
    letter-spacing: 3px;
    white-space: nowrap;
  }

  .tagline {
    position: absolute;
    left: 0;
    width: 1222px;
    top: 456px;
    text-align: center;
    font-size: 32px;
    font-style: italic;
    letter-spacing: 1px;
    line-height: 1;
    white-space: nowrap;
  }
</style>
</head>
<body>
  <main class="card">
    <div class="brand-mark"><span class="dot"></span>Tempoquintal</div>
    <p class="shop-label">online shop</p>
    <h1 class="shop-name">Tempoquintal</h1>
    <p class="tagline">VINTAGE WATCHES FOR ALL GENERATIONS</p>
  </main>
</body>
</html>
```